Insurance Agency Flyer
8.5 x 11 Double Sided Full Color
Bluelanem your draft #10 is good except that due to trademark issues we must display the insurance company logos across the bottom on a white background only. The overall design is sleek but the blue background under the logos would be a deal breaker. I like the idea of using a house and car also but not that particular house, car and people. Good examples of the kinds of photos we are seeking are those seen in draft #5 and draft #6
@PH - please check your private message on right top once you login.
Thanks
Ravenwood, draft #3 is good. Can you try changing the font color and/or size and/or style of certain words in the "why are you paying so much for auto insurance" line? For example in draft #2, auto insurance stands out more because it is in a different color. I would be curious to see what other options there are to make those words stand out.
Tobel, I like draft #2 however can you make the following modifications:
1. Please note that while we are allowed to use the "Lakemount" logo we can't use their symbols for the Auto, home, motorcycle... etc. Could you replace those symbols with something similar?
2. The CMQ logo should be placed somewhere else as this is not one of our insurance but rather an organization we belong to (for example in draft #1 it is listed on the bottom right).
3. Also, could our phone number be more pronounced somewhere?
4. And finally, I like the overall clean layout but not crazy about that particular guy and car. Any other options?
Ravnewood, I really like draft #1. I would be inetrested to see how it might look if the auto, home, motorcycle... icons were also across the very top of page 1? Also, Is there a way to put more emphasis on the words "auto insurance" justs o that they stand out more, maybe more than the "Paying so Much".

```html
<!DOCTYPE html>
<html lang="en">
<head>
<meta charset="utf-8">
<title>KRV Coverage Agency – Flyer</title>
<link href="https://fonts.googleapis.com/css2?family=Source+Sans+3:wght@400;600;700&display=swap" rel="stylesheet">
<style>
  :root{
    --stage:#e9e6e1;
    --paper:#ffffff;
    --blue:#1f6fb2;
    --navy:#1b3f6b;
    --orange:#f08a1c;
    --ink:#3a3a3a;
    --muted:#6b6b6b;
    --rule:#d5dde6;
    --icon:#2c77b8;
  }
  *{box-sizing:border-box;margin:0;padding:0}
  html,body{width:1200px;height:927px;overflow:hidden;background:var(--stage)}
  body{font-family:"Source Sans 3",Arial,sans-serif;color:var(--ink);position:relative}
  .page{position:absolute;top:108px;width:550px;height:712px;background:var(--paper);
        box-shadow:0 2px 8px rgba(0,0,0,.18);overflow:hidden}
  .page--front{left:35px}
  .page--back{left:615px}

  .coverage-strip{display:flex;justify-content:center;gap:22px;height:46px;padding-top:6px;background:var(--paper)}
  .coverage-item{display:flex;flex-direction:column;align-items:center;width:40px}
  .coverage-item svg{width:30px;height:22px}
  .coverage-item span{font-size:7px;color:var(--muted);margin-top:2px;text-transform:uppercase;letter-spacing:.3px}

  /* front */
  .front-headline{text-align:center;font-size:27px;line-height:1.12;color:var(--blue);font-weight:600;padding:12px 20px 8px}
  .front-headline em,.back-headline em{font-style:normal;color:var(--orange)}
  .front-photo{height:310px;background:linear-gradient(180deg,#cfe3f1 0%,#9fb9cf 45%,#2d3a47 100%)}
  .front-tagline{font-size:22px;color:var(--blue);font-weight:600;padding:10px 28px 4px;border-top:3px solid var(--blue)}
  .front-tagline em{font-style:normal;color:var(--orange)}
  .front-body{display:flex;padding:4px 28px 0;gap:20px}
  .benefits h3{font-size:10px;color:var(--blue);font-weight:700;margin-bottom:3px}
  .benefits ul{list-style:none}
  .benefits li{font-size:9.5px;line-height:1.45;padding-left:10px;position:relative}
  .benefits li::before{content:"";position:absolute;left:0;top:5px;width:4px;height:4px;background:var(--orange);border-radius:50%}
  .front-brand{margin-left:auto;text-align:center;padding-top:20px}
  .brand-mark{display:flex;align-items:center;gap:7px;color:var(--navy);font-weight:700;font-size:19px;line-height:1}
  .brand-mark i{display:block;width:14px;height:14px;border-radius:50%;background:var(--navy)}
  .front-phone{font-size:30px;color:var(--navy);font-weight:700;margin-top:10px}
  .front-footer{position:absolute;left:0;right:0;bottom:0;height:32px;border-top:1px solid var(--rule);
                font-size:9.5px;color:var(--muted);padding:10px 28px}

  /* back */
  .back-hero{position:relative;height:392px;background:linear-gradient(180deg,#dfeef8 0%,#bcd9ee 55%,#a9c3d6 100%)}
  .back-headline{position:absolute;left:26px;top:22px;font-size:44px;line-height:1.03;color:var(--blue);font-weight:600}
  .back-headline em{font-size:52px}
  .back-promise{font-size:19px;color:var(--orange);font-weight:600;padding:10px 26px 4px;border-top:3px solid var(--blue)}
  .back-body{display:flex;padding:4px 26px 0;gap:14px}
  .back-body .benefits{flex:1}
  .benefit-cols{display:flex;gap:14px}
  .back-contact{display:flex;gap:14px;padding:16px 26px 0;align-items:flex-start}
  .contact-block{font-size:10px;line-height:1.35;color:var(--ink)}
  .contact-block strong{display:block;font-size:17px;color:var(--navy)}
  .membership-badge{margin-left:auto;width:42px;height:54px;background:var(--navy)}
  .carrier-row{position:absolute;left:0;right:0;bottom:0;height:44px;border-top:1px solid var(--rule);
               display:flex;justify-content:space-around;align-items:center;padding:0 18px;background:var(--paper)}
  .carrier-row span{font-size:11px;font-weight:700;color:var(--navy)}
</style>
</head>
<body>
<svg width="0" height="0" style="position:absolute">
  <symbol id="car-icon" viewBox="0 0 30 22">
    <rect x="1" y="1" width="28" height="20" rx="4" fill="var(--icon)"/>
    <path d="M6 14h18v-3l-3-4H10l-3 4H6z" fill="#fff"/>
    <circle cx="10" cy="15" r="2" fill="#fff"/><circle cx="20" cy="15" r="2" fill="#fff"/>
  </symbol>
</svg>

<section class="page page--front">
  <nav class="coverage-strip">
    <div class="coverage-item"><svg><use href="#car-icon"/></svg><span>Auto</span></div>
    <div class="coverage-item"><svg><use href="#car-icon"/></svg><span>Home</span></div>
    <div class="coverage-item"><svg><use href="#car-icon"/></svg><span>Cycle</span></div>
    <div class="coverage-item"><svg><use href="#car-icon"/></svg><span>Boat</span></div>
    <div class="coverage-item"><svg><use href="#car-icon"/></svg><span>RV</span></div>
    <div class="coverage-item"><svg><use href="#car-icon"/></svg><span>Life</span></div>
    <div class="coverage-item"><svg><use href="#car-icon"/></svg><span>Business</span></div>
  </nav>
  <h1 class="front-headline">Why are you <em>paying</em> so much<br>for <em>auto insurance?</em></h1>
  <div class="front-photo" role="img" aria-label="Photo of a smiling couple holding car keys beside their new car under a bright sky"></div>
  <p class="front-tagline">Let KRV <em>lower</em> your auto insurance bill!</p>
  <div class="front-body">
    <div class="benefits">
      <h3>How does KRV do it?</h3>
      <ul>
        <li>Find discounts you may be missing</li>
        <li>Comparison shop with multiple companies on your behalf</li>
        <li>Package policies for even more savings</li>
        <li>Find ways to reduce or eliminate fees</li>
        <li>KRV has NO agency fees</li>
        <li>Customize a policy just for you</li>
      </ul>
    </div>
    <div class="front-brand">
      <div class="brand-mark"><i></i>KRV Coverage Agency</div>
      <div class="front-phone">(555) 318-2046</div>
    </div>
  </div>
  <footer class="front-footer">KRV Coverage Agency, 2280-B Linden Crest Rd, Oakvale, NC 28990 | www.krvcoverage.com</footer>
</section>

<section class="page page--back">
  <nav class="coverage-strip">
    <div class="coverage-item"><svg><use href="#car-icon"/></svg><span>Auto</span></div>
    <div class="coverage-item"><svg><use href="#car-icon"/></svg><span>Home</span></div>
    <div class="coverage-item"><svg><use href="#car-icon"/></svg><span>Cycle</span></div>
    <div class="coverage-item"><svg><use href="#car-icon"/></svg><span>Boat</span></div>
    <div class="coverage-item"><svg><use href="#car-icon"/></svg><span>RV</span></div>
    <div class="coverage-item"><svg><use href="#car-icon"/></svg><span>Life</span></div>
    <div class="coverage-item"><svg><use href="#car-icon"/></svg><span>Business</span></div>
  </nav>
  <div class="back-hero" role="img" aria-label="Photo of a happy young couple, the woman riding piggyback, against a light blue sky">
    <h1 class="back-headline">Call KRV before<br><em>paying</em><br>your next<br><em>insurance</em><br>bill</h1>
  </div>
  <p class="back-promise">Save money without cutting coverage or service</p>
  <div class="back-body">
    <div class="benefits">
      <h3>How does KRV do it?</h3>
      <div class="benefit-cols">
        <ul><li>24/7 Claims Service</li><li>Guaranteed claims repairs</li></ul>
        <ul><li>Local Agent</li><li>A-Rated CMQ Accredited Business</li></ul>
        <ul><li>Variety of discounts available</li><li>Friendly, knowledgeable agents</li></ul>
      </div>
    </div>
  </div>
  <div class="back-contact">
    <div class="brand-mark"><i></i>KRV Coverage Agency</div>
    <div class="contact-block">
      <strong>(555) 318-2046</strong>
      KRV Coverage Agency<br>2280-B Linden Crest Rd,<br>Oakvale, NC 28990<br>www.krvcoverage.com
    </div>
    <div class="membership-badge" role="img" aria-label="CMQ accredited member badge"></div>
  </div>
  <div class="carrier-row">
    <span>Harlow Insurance</span><span>Vestra</span><span>Corvane Auto &amp; Home</span><span>Lakemount</span><span>Maribel</span>
  </div>
</section>
</body>
</html>
```